ALL TEXT Social Media Graphics

We are looking for a series of social media graphics for Instagram (new size: 4:5 (1080 x 1350 pixels) ratio that are ALL TEXT. We want the following quotes below on each graphic; one quote per graphic. AND, In very small letters at the bottom of each graphic, add @PaulaWrenLive
The look and feel of these graphics should be complimentary to the color palette attached below; but keep them simple. But the design is up to you; at the end of this document, I provided various samples of all text graphics that I like as examples.
The Quotes are in the attached WORD document
women trying to lose weight

```html
<!DOCTYPE html>
<html lang="en">
<head>
<meta charset="utf-8">
<title>Sun Glow Summer Reset – Quote Series</title>
<link rel="stylesheet" href="https://fonts.googleapis.com/css2?family=Libre+Franklin:ital,wght@0,400;0,800;1,800&display=swap">
<style>
  :root {
    --board: #231f20;
    --card-top: #ffffff;
    --card-glow: #fddcec;
    --pink: #e8559a;
    --berry: #b0155d;
  }
  * { margin: 0; padding: 0; box-sizing: border-box; }
  html, body { width: 1200px; height: 600px; overflow: hidden; background: var(--board); }
  body { font-family: "Libre Franklin", Arial, sans-serif; position: relative; }

  .quote-card {
    position: absolute;
    width: 216px;
    height: 270px;
    background: linear-gradient(150deg, var(--card-top) 55%, var(--card-glow) 100%);
    white-space: nowrap;
    overflow: hidden;
  }
  .quote-card > * { position: absolute; left: 20px; }

  .headline {
    top: 14px;
    font-weight: 800;
    font-size: 18.6px;
    line-height: 22.4px;
    color: var(--pink);
  }
  .headline-accent {
    font-weight: 800;
    font-size: 18.6px;
    line-height: 22.4px;
    color: var(--berry);
  }
  .pitch {
    font-weight: 800;
    font-style: italic;
    font-size: 17.4px;
    line-height: 20.4px;
    color: var(--berry);
  }
  .pitch .hl { color: var(--pink); }
  .call-to-action {
    font-weight: 400;
    font-size: 15.4px;
    line-height: 17.3px;
    color: var(--pink);
  }
  .handle {
    top: 253px;
    font-weight: 800;
    font-size: 6.8px;
    color: var(--berry);
  }
  .row-1 { top: 25px; }
  .row-2 { top: 305px; }
  .col-1 { left: 40px; } .col-2 { left: 266px; } .col-3 { left: 492px; }
  .col-4 { left: 718px; } .col-5 { left: 944px; }
</style>
</head>
<body>

<article class="quote-card row-1 col-1">
  <p class="headline">Don't wait 'til next<br>summer to get<br>right.</p>
  <p class="headline-accent" style="top:86px">The time is NOW.</p>
  <p class="pitch" style="top:132px"><span class="hl">Drop 30 pounds</span><br>with the Sun Glow<br>Summer Reset.</p>
  <p class="call-to-action" style="top:218px">Comment “Summer”!</p>
  <p class="handle">@PaulaWrenLive</p>
</article>

<article class="quote-card row-1 col-2">
  <p class="headline">Sis, we're dropping<br>belly flat and<br>saying goodbye<br>to stubborn<br>pounds.</p>
  <p class="pitch" style="top:153px">Join the Sun Glow<br>Summer Reset —</p>
  <p class="call-to-action" style="top:218px">comment “Summer”!</p>
  <p class="handle">@PaulaWrenLive</p>
</article>

<article class="quote-card row-1 col-3">
  <p class="headline">Snatched waist,<br>flat tummy,<br>30 pounds lighter —</p>
  <p class="pitch" style="top:102px">that's what the<br>Sun Glow Summer<br>Reset<br>Challenge delivers.</p>
  <p class="call-to-action" style="top:200px">Comment “Sun Glow”<br>to get the plan</p>
  <p class="handle">@PaulaWrenLive</p>
</article>

<article class="quote-card row-1 col-4">
  <p class="headline">There's still time<br>to drop the<br>30 pounds and slay<br>this summer.</p>
  <p class="pitch" style="top:130px">The Sun Glow<br>Summer Reset<br>has the blueprint.</p>
  <p class="call-to-action" style="top:218px">Comment “Sun Glow”!</p>
  <p class="handle">@PaulaWrenLive</p>
</article>

<article class="quote-card row-1 col-5">
  <p class="headline">If your goal is<br>a tiny waist,<br>flat belly,<br>and 30 pounds<br>down —</p>
  <p class="pitch" style="top:146px">this is the plan.</p>
  <p class="call-to-action" style="top:184px">Comment “Summer”<br>to join the Sun Glow<br>Summer Reset!</p>
  <p class="handle">@PaulaWrenLive</p>
</article>

<article class="quote-card row-2 col-1">
  <p class="headline">You can absolutely<br>be down 20–30<br>pounds by end<br>of summer.</p>
  <p class="pitch" style="top:113px">All it takes is the<br>right plan — and<br>you've found it.</p>
  <p class="call-to-action" style="top:183px">Comment “Sun Glow”<br>for the Sun Glow<br>Summer Reset!</p>
  <p class="handle">@PaulaWrenLive</p>
</article>

<article class="quote-card row-2 col-2">
  <p class="headline">You don't need<br>another diet —<br>you need a system<br>that works.</p>
  <p class="pitch" style="top:120px"><span class="hl">Drop 30 pounds</span><br>with the Sun Glow<br>Summer Reset.</p>
  <p class="call-to-action" style="top:200px">Comment “Summer”<br>to start now.</p>
  <p class="handle">@PaulaWrenLive</p>
</article>

<article class="quote-card row-2 col-3">
  <p class="headline">Nothing feels<br>better than seeing<br>that scale drop<br>week after week.</p>
  <p class="pitch" style="top:114px">Let's lose up to<br>30 pounds this<br>summer — together.</p>
  <p class="call-to-action" style="top:183px">Comment “Summer”<br>to join the Sun Glow<br>Summer Reset!</p>
  <p class="handle">@PaulaWrenLive</p>
</article>

<article class="quote-card row-2 col-4">
  <p class="headline">You've got 8 weeks<br>and the perfect<br>plan to drop<br>30 pounds.</p>
  <p class="pitch" style="top:121px">Let's get snatched<br>this summer with<br>the Sun Glow<br>Summer Reset.</p>
  <p class="call-to-action" style="top:217px">Comment “Summer”!</p>
  <p class="handle">@PaulaWrenLive</p>
</article>

<article class="quote-card row-2 col-5">
  <p class="headline">This summer ain't<br>over — and neither<br>are your body goals.</p>
  <p class="pitch" style="top:111px"><span class="hl">Drop 30 pounds</span><br>with the Sun Glow<br>Summer Reset.</p>
  <p class="call-to-action" style="top:200px">Comment “Sun Glow”<br>to get the plan</p>
  <p class="handle">@PaulaWrenLive</p>
</article>

</body>
</html>
```